Supplement Rebranding Bottle Design

READ WORD DOCUMENT ATTACHED.
We want to rebrand our current health supplements (see below). We do want it to be modern, vibrant and appealing. Very upscale and elegant as it targets primarily women.
Bottle size: see pictures for bottle size, along with sample bottles that we like; we’re open to any bottle similar to the ones attached.
Current bottles: So ideally, we’d keep the core color on each bottle with a new branding/bottle design. But we're open to your suggestion.

Target Market(s)

mostly women but shouldn't be overly feminine

Requirements
Must have
• see bottle sizes attached

```html
<!DOCTYPE html>
<html lang="en">
<head>
<meta charset="utf-8">
<title>Hepa Balance – Rejuvenating Cleanse &amp; Detox Label</title>
<link href="https://fonts.googleapis.com/css2?family=Roboto:wght@300;400&family=Roboto+Condensed:wght@700&family=Montserrat:wght@500&display=swap" rel="stylesheet">
<style>
  :root {
    --page-bg: #f4f3f6;
    --label-top: #8d66a6;
    --label-mid: #6f4f96;
    --label-bottom: #54417f;
    --text-light: #ece6f2;
    --text-soft: #d9cfe4;
    --accent-green: #b9d98c;
    --rule: #cdbfdc;
  }
  * { margin: 0; padding: 0; box-sizing: border-box; }
  html, body {
    width: 1200px;
    height: 3599px;
    overflow: hidden;
    background: var(--page-bg);
  }
  .canvas {
    position: relative;
    width: 1200px;
    height: 3599px;
    display: flex;
    align-items: center;
    justify-content: center;
  }
  .label {
    position: relative;
    width: 900px;
    height: 1480px;
    border-radius: 36px;
    background: linear-gradient(180deg, var(--label-top) 0%, var(--label-mid) 55%, var(--label-bottom) 100%);
    padding: 0 100px;
    color: var(--text-light);
  }
  .brand-name {
    position: absolute;
    top: 230px;
    left: 0;
    right: 0;
    text-align: center;
    font-family: "Montserrat", sans-serif;
    font-weight: 500;
    font-size: 52px;
    letter-spacing: 0.32em;
    color: var(--text-light);
  }
  .product-block {
    position: absolute;
    left: 100px;
    right: 100px;
    bottom: 150px;
  }
  .product-title {
    font-family: "Roboto", sans-serif;
    font-weight: 300;
    font-size: 86px;
    line-height: 1.08;
    color: var(--text-light);
    padding-bottom: 22px;
    border-bottom: 2px solid var(--rule);
  }
  .diet-claim {
    font-family: "Roboto", sans-serif;
    font-weight: 400;
    font-size: 36px;
    color: var(--accent-green);
    padding: 18px 0 20px;
    border-bottom: 2px solid var(--rule);
  }
  .benefits {
    font-family: "Roboto", sans-serif;
    font-weight: 300;
    font-size: 33px;
    line-height: 1.4;
    color: var(--text-soft);
    padding: 22px 0 22px;
    border-bottom: 2px solid var(--rule);
  }
  .benefits .dot { padding: 0 10px; }
  .contents {
    font-family: "Roboto Condensed", sans-serif;
    font-weight: 700;
    font-size: 32px;
    line-height: 1.45;
    color: var(--text-soft);
    padding-top: 22px;
  }
</style>
</head>
<body>
  <main class="canvas">
    <section class="label">
      <p class="brand-name">HEPA BALANCE</p>
      <div class="product-block">
        <h1 class="product-title">Rejuvenating<br>Cleanse &amp; Detox</h1>
        <p class="diet-claim">VEGAN &amp; GLUTEN FREE</p>
        <p class="benefits">Supports Liver Health<span class="dot">•</span>Antioxidant Support<br>Promotes Liver Detoxification</p>
        <p class="contents">DIETARY SUPPLEMENT<br>120 VEGETABLE CAPSULES</p>
      </div>
    </section>
  </main>
</body>
</html>
```